Rinsely Surface Cleaning - Business Card Design

Use company logo and design a new business card. We are looking for a front and back design. The back should be a dark purple background. We want the back to show cartoon-like soap bubbles chasing mildew cartoon shaped figures. This gives the idea that Rinsely Surface Cleaning provides exterior washing services that work. No mildew stands a chance when Rinsely Surface Cleaning shows up to work. The mildew cartoon images should be green in color, have eyes, and look scared of the bubbles. The bubbles should be light blue in color and have eyes that looked excited to be there.
We will advertise on Chatterly and Pixalonia. These Chatterly and Pixalonia icons should be somewhere on the card.

```html
<!DOCTYPE html>
<html lang="en">
<head>
<meta charset="UTF-8">
<title>Rinsely Surface Cleaning – Business Card</title>
<link href="https://fonts.googleapis.com/css2?family=Montserrat:wght@400;500;700;800&display=swap" rel="stylesheet">
<style>
  :root {
    --page-bg: #1c1c1f;
    --brand-purple: #2e1a5e;
    --brand-purple-deep: #24124d;
    --mildew-green: #3fbf3a;
    --mildew-glow: #2f7a5a;
    --card-white: #ffffff;
    --text-dark: #2e1a5e;
    --text-body: #3a2a66;
  }
  * { box-sizing: border-box; margin: 0; padding: 0; }
  html, body {
    width: 1200px; height: 948px; overflow: hidden;
    background: var(--page-bg);
    font-family: "Montserrat", Arial, sans-serif;
  }
  .canvas { position: relative; width: 1200px; height: 948px; }
  .card {
    position: absolute; left: 230px; width: 740px; height: 420px;
    border-radius: 28px; overflow: hidden;
  }
  /* Back side */
  .card-back { top: 34px; background: var(--brand-purple); }
  .back-illustration {
    position: absolute; inset: 0;
    background:
      radial-gradient(ellipse 140px 90px at 78% 30%, var(--mildew-green) 0%, var(--mildew-glow) 60%, transparent 100%),
      radial-gradient(ellipse 110px 70px at 18% 82%, var(--mildew-green) 0%, var(--mildew-glow) 60%, transparent 100%),
      radial-gradient(ellipse 80px 55px at 86% 88%, var(--mildew-green) 0%, transparent 100%),
      radial-gradient(ellipse 70px 45px at 12% 20%, var(--mildew-glow) 0%, transparent 100%),
      radial-gradient(ellipse 90px 60px at 50% 12%, var(--mildew-glow) 0%, transparent 100%),
      linear-gradient(135deg, var(--brand-purple) 0%, var(--brand-purple-deep) 100%);
  }
  .back-logo {
    position: absolute; inset: 0;
    display: flex; flex-direction: column; align-items: center; justify-content: center;
    color: var(--card-white); font-weight: 800; text-align: center;
  }
  .back-logo .brand-main { font-size: 96px; line-height: 1; letter-spacing: -2px; }
  .back-logo .brand-sub { font-size: 26px; letter-spacing: 2px; margin-top: 10px; }

  /* Front side */
  .card-front { top: 494px; background: var(--card-white); color: var(--text-body); }
  .front-logo {
    position: absolute; left: 48px; top: 56px;
    color: var(--text-dark); font-weight: 800;
  }
  .front-logo .brand-main { font-size: 72px; line-height: 1; letter-spacing: -2px; }
  .front-logo .brand-sub { font-size: 18px; letter-spacing: 1.5px; margin-top: 6px; }
  .address {
    position: absolute; left: 48px; top: 196px;
    font-size: 17px; line-height: 1.45; font-weight: 400;
  }
  .rule { position: absolute; height: 2px; background: var(--text-dark); }
  .rule-address { left: 48px; top: 262px; width: 260px; }
  .rule-name { left: 360px; top: 126px; width: 330px; }
  .contact-list { position: absolute; left: 48px; top: 280px; list-style: none; }
  .contact-list li {
    display: flex; align-items: center; gap: 12px;
    font-size: 18px; line-height: 1.6;
  }
  .contact-list svg { width: 17px; height: 17px; fill: var(--text-dark); flex: none; }
  .person { position: absolute; right: 50px; top: 46px; text-align: right; }
  .person-name { font-size: 30px; font-weight: 800; color: var(--text-dark); letter-spacing: 0.5px; }
  .person-title { font-size: 18px; font-weight: 500; margin-top: 2px; }
  .social-list {
    position: absolute; right: 50px; bottom: 40px; list-style: none; text-align: right;
  }
  .social-list li {
    display: flex; align-items: center; justify-content: flex-end; gap: 8px;
    font-size: 14px; font-weight: 500; color: var(--text-dark); line-height: 1.7;
  }
  .social-list .dot { width: 14px; height: 14px; border-radius: 50%; background: var(--text-dark); }
</style>
</head>
<body>
<div class="canvas">

  <section class="card card-back">
    <div class="back-illustration" role="img" aria-label="Cartoon scene of green mildew creatures scattered over a dark purple background"></div>
    <div class="back-logo">
      <div class="brand-main">Rinsely</div>
      <div class="brand-sub">SURFACE CLEANING</div>
    </div>
  </section>

  <section class="card card-front">
    <div class="front-logo">
      <div class="brand-main">Rinsely</div>
      <div class="brand-sub">SURFACE CLEANING</div>
    </div>

    <p class="address">Your address, City<br>State, Zip 12506</p>
    <div class="rule rule-address"></div>

    <ul class="contact-list">
      <li>
        <svg viewBox="0 0 24 24"><path d="M6.6 10.8a15.1 15.1 0 0 0 6.6 6.6l2.2-2.2a1 1 0 0 1 1-.25 11.4 11.4 0 0 0 3.6.57 1 1 0 0 1 1 1V20a1 1 0 0 1-1 1A17 17 0 0 1 3 4a1 1 0 0 1 1-1h3.5a1 1 0 0 1 1 1c0 1.25.2 2.45.57 3.6a1 1 0 0 1-.25 1z"/></svg>
        123 456 789
      </li>
      <li>
        <svg viewBox="0 0 24 24"><path d="M2 5h20v14H2z M2 5l10 8 10-8" fill="none" stroke="#2e1a5e" stroke-width="2"/></svg>
        info@yourmailbox.com
      </li>
      <li>
        <svg viewBox="0 0 24 24"><circle cx="12" cy="12" r="9" fill="none" stroke="#2e1a5e" stroke-width="2"/><path d="M3 12h18M12 3c3 3 3 15 0 18M12 3c-3 3-3 15 0 18" fill="none" stroke="#2e1a5e" stroke-width="1.6"/></svg>
        www.yourwebsite.com
      </li>
    </ul>

    <div class="person">
      <div class="person-name">MARCUS HALE</div>
      <div class="person-title">Managing Director</div>
    </div>
    <div class="rule rule-name"></div>

    <ul class="social-list">
      <li><span class="dot"></span>Chatterly</li>
      <li><span class="dot"></span>Pixalonia</li>
    </ul>
  </section>

</div>
</body>
</html>
```